Thai Takeaway Menu Design

I need a menu re-design for a thai takeaway/restaurant in australia.

Please use content from the existing menu
http://www.platterwink.example/u/menu/7302918?p=1

I'd like to emphasise on
1 - free delivery for order over $40
2 - gluten free and vegetatian option available on most meal (however you want to word it - not fuss)

*remove (the banner order online and save $10)

I'm happy to change the whole concept & design. I particularly like rustic, raw look more than moden ones. Does not need to be flowery or anything like current one :)

Industry/Entity Type

Restaurant

```html
<!DOCTYPE html>
<html lang="en">
<head>
<meta charset="utf-8">
<title>Sawan Traditional Thai Cuisine – Menu</title>
<link href="https://fonts.googleapis.com/css2?family=Montserrat:wght@800&family=Nunito:wght@800&family=Quicksand:wght@400;500&display=swap" rel="stylesheet">
<style>
:root{
  --stage:#000000;
  --paper-light:#b97e48;
  --paper-mid:#a06a3a;
  --paper-dark:#7a4a22;
  --fold:rgba(60,32,12,.45);
  --ink:#e3c8a2;
  --ink-soft:rgba(236,214,182,.82);
  --white:#ffffff;
  --accent:#f4e21a;
  --ornament:rgba(52,28,10,.55);
  --swirl:rgba(250,236,214,.55);
  --brand:#8a6a45;
}
*{margin:0;padding:0;box-sizing:border-box}
html,body{width:780px;height:1200px;overflow:hidden;background:var(--stage)}
body{position:relative;font-family:"Quicksand",sans-serif;color:var(--ink)}
.sheet{position:absolute;background:
  radial-gradient(ellipse at 40% 45%,var(--paper-light) 0%,var(--paper-mid) 55%,var(--paper-dark) 100%);}
.sheet--outside{left:58px;top:62px;width:660px;height:510px}
.sheet--inside{left:64px;top:618px;width:658px;height:512px}
.fold{position:absolute;top:0;bottom:0;width:1px;background:var(--fold)}
.corner{position:absolute;width:38px;height:38px;background:var(--ornament);border-radius:6px;opacity:.55}
.bracket{position:absolute;width:12px;background:var(--ornament);border-radius:6px;opacity:.7}
.abs{position:absolute}
.deal-title{font-family:"Nunito",sans-serif;font-weight:800;color:var(--white);font-size:16px;letter-spacing:.4px;white-space:nowrap}
.deal-items{font-size:9.5px;line-height:12px;color:var(--ink-soft)}
.deal-price{font-size:13px;color:var(--ink)}
.deal-rule{height:2px;background:#3b1f0c}
.notice{color:var(--accent);font-size:12px;line-height:16px;text-align:center}
.hours{text-align:center}
.hours h3{font-weight:400;font-size:17px;color:var(--ink);margin-bottom:4px}
.hours p{font-size:8.5px;line-height:11.5px;color:var(--ink-soft)}
.cover{position:absolute;left:442px;top:0;width:218px;height:510px;text-align:center}
.frame{position:absolute;left:8px;width:200px;height:38px;border:2px solid #3b1f0c}
.frame--top{top:40px;border-bottom:none}
.frame--bottom{top:442px;border-top:none}
.flourish{position:absolute;left:50%;transform:translateX(-50%);width:76px;height:22px;background:var(--ornament);border-radius:11px;opacity:.7}
.brand{font-family:"Nunito",sans-serif;font-weight:800;color:var(--brand);font-size:34px;letter-spacing:3px;line-height:1}
.tagline{font-size:9px;color:#3e230e}
.menu-word{font-family:"Montserrat",sans-serif;font-weight:800;color:var(--white);font-size:64px;letter-spacing:-1px;line-height:1}
.cover-sub{font-size:13px;color:var(--ink)}
.address{font-size:11px;line-height:14px;color:var(--ink)}
.section-title{position:absolute;font-family:"Nunito",sans-serif;font-weight:800;color:var(--white);font-size:12px;letter-spacing:.5px;display:flex;align-items:center;gap:6px}
.swirl{display:inline-block;width:62px;height:12px;border-radius:6px;background:var(--swirl);opacity:.35}
.dish-list{position:absolute;list-style:none;font-size:9.3px;line-height:12px;color:var(--ink-soft)}
.dish-list li{display:flex;justify-content:space-between;white-space:nowrap}
.dish-list .price{text-align:right}
.col1{left:13px;width:207px}
.col2{left:238px;width:196px}
.col3{left:463px;width:189px}
.dietary{position:absolute;left:242px;top:449px;font-family:"Nunito",sans-serif;font-weight:800;color:var(--white);font-size:10px;line-height:12px}
.brand--small{position:absolute;left:440px;width:218px;top:456px;text-align:center;font-size:24px}
</style>
</head>
<body>

<section class="sheet sheet--outside" aria-label="Menu outside">
  <div class="fold" style="left:221px"></div>
  <div class="fold" style="left:442px"></div>

  <span class="corner" role="img" aria-label="corner flourish" style="left:4px;top:4px"></span>
  <span class="corner" role="img" aria-label="corner flourish" style="left:180px;top:4px"></span>
  <span class="corner" role="img" aria-label="corner flourish" style="left:4px;top:468px"></span>
  <span class="corner" role="img" aria-label="corner flourish" style="left:180px;top:468px"></span>
  <span class="corner" role="img" aria-label="corner flourish" style="left:225px;top:4px"></span>
  <span class="corner" role="img" aria-label="corner flourish" style="left:400px;top:4px"></span>
  <span class="corner" role="img" aria-label="corner flourish" style="left:225px;top:468px"></span>
  <span class="corner" role="img" aria-label="corner flourish" style="left:400px;top:468px"></span>

  <span class="bracket" role="img" aria-label="scroll bracket" style="left:25px;top:100px;height:92px"></span>
  <h2 class="deal-title abs" style="left:45px;top:95px">DINNER for TWO</h2>
  <p class="deal-items abs" style="left:55px;top:124px">Spring Rools (4)<br>Chicken &amp; Cashew Nuts<br>Massaman Curry<br>Rice</p>
  <span class="deal-price abs" style="left:140px;top:170px">$28</span>
  <span class="deal-rule abs" style="left:112px;top:186px;width:73px"></span>

  <span class="bracket" role="img" aria-label="scroll bracket" style="left:25px;top:263px;height:96px"></span>
  <h2 class="deal-title abs" style="left:45px;top:259px">FAMILY PACK</h2>
  <p class="deal-items abs" style="left:55px;top:287px">Spring Rools (4)<br>Satay Chicken (4)<br>Chicken &amp; Cashew Nuts<br>Red Curry Beef<br>Pad Thai<br>Rice(L)</p>
  <span class="deal-price abs" style="left:142px;top:341px">$45</span>
  <span class="deal-rule abs" style="left:112px;top:356px;width:73px"></span>

  <span class="bracket" role="img" aria-label="scroll bracket" style="left:231px;top:148px;height:98px"></span>
  <h2 class="deal-title abs" style="left:254px;top:144px">LUNCH SPECIAL $10</h2>
  <p class="deal-items abs" style="left:262px;top:172px">Pad Thai<br>Sweet and Sour Pork /w Rice<br>Chicken &amp; Cashew Nuts /w Rice<br>Green Curry Chicken / w Rice<br>Beef noodle Soup</p>
  <p class="deal-items abs" style="left:262px;top:245px">FREE CAN OF SOFT DRINK</p>

  <p class="notice abs" style="left:221px;width:221px;top:298px">FREE DELIVERY WITH IN 5KM-<br>MINIMUM ORDERS $40</p>

  <div class="hours abs" style="left:221px;width:221px;top:347px">
    <h3>Trading Hours</h3>
    <p>Lunch ( Wednesday - Sunday) : 11.00 - 2.30 PM<br>Dinner ( 7 days ) : 5.00 - 9.30PM</p>
  </div>

  <div class="cover">
    <span class="flourish" role="img" aria-label="crown flourish" style="top:14px"></span>
    <span class="frame frame--top"></span>
    <div class="abs" style="left:0;width:218px;top:94px">
      <div class="brand">SAWAN</div>
      <div class="tagline" style="margin-top:4px">Traditional Thai Cuisine</div>
    </div>
    <div class="menu-word abs" style="left:0;width:218px;top:150px">MENU</div>
    <p class="cover-sub abs" style="left:0;width:218px;top:216px">Dine In, Takeaway &amp; Delivery</p>
    <p class="notice abs" style="left:0;width:218px;top:235px">*Free delivery with in 5km-<br>minimum orders $40</p>
    <div class="hours abs" style="left:0;width:218px;top:298px">
      <h3>Trading Hours</h3>
      <p>Lunch ( Wednesday - Sunday) : 11.00 - 2.30 PM<br>Dinner ( 7 days ) : 5.00 - 9.30PM</p>
    </div>
    <p class="address abs" style="left:0;width:218px;top:401px">27 Kestrel Road, Oakvale<br>Corner of Linden St. and Kestrel Rd.<br>Phone 07 3190 4417</p>
    <span class="frame frame--bottom"></span>
    <span class="flourish" role="img" aria-label="scroll flourish" style="top:470px"></span>
  </div>
</section>

<section class="sheet sheet--inside" aria-label="Menu inside">
  <div class="fold" style="left:220px"></div>
  <div class="fold" style="left:440px"></div>

  <span class="corner" role="img" aria-label="corner flourish" style="left:4px;top:4px"></span>
  <span class="corner" role="img" aria-label="corner flourish" style="left:178px;top:4px"></span>
  <span class="corner" role="img" aria-label="corner flourish" style="left:178px;top:470px"></span>
  <span class="corner" role="img" aria-label="corner flourish" style="left:224px;top:4px"></span>
  <span class="corner" role="img" aria-label="corner flourish" style="left:398px;top:4px"></span>
  <span class="corner" role="img" aria-label="corner flourish" style="left:224px;top:470px"></span>
  <span class="corner" role="img" aria-label="corner flourish" style="left:398px;top:470px"></span>
  <span class="corner" role="img" aria-label="corner flourish" style="left:444px;top:4px"></span>
  <span class="corner" role="img" aria-label="corner flourish" style="left:616px;top:4px"></span>
  <span class="corner" role="img" aria-label="corner flourish" style="left:444px;top:470px"></span>
  <span class="corner" role="img" aria-label="corner flourish" style="left:616px;top:470px"></span>

  <h2 class="section-title" style="left:13px;top:56px">ENTREE <span class="swirl" role="img" aria-label="swirl ornament"></span></h2>
  <ul class="dish-list col1" style="top:82px">
    <li><span>Spring Rools * (4)</span><span class="price">$6.00</span></li>
    <li><span>Satay Chicken (4)</span><span class="price">$6.00</span></li>
    <li><span>Fish Cakes (4)</span><span class="price">$6.00</span></li>
    <li><span>Dim Sim (4)</span><span class="price">$6.00</span></li>
    <li><span>Duck Rice Paper Rolls * (2)</span><span class="price">$6.00</span></li>
    <li><span>papaya salad</span><span class="price">$6.00</span></li>
    <li><span>Tofu/ w Peanut sause *</span><span class="price">$6.00</span></li>
  </ul>
  <h2 class="section-title" style="left:15px;top:169px">SOUP <span class="swirl" role="img" aria-label="swirl ornament"></span></h2>
  <ul class="dish-list col1" style="top:196px;left:15px;width:205px">
    <li><span>Tom Yum Praw *</span><span class="price">$7.00</span></li>
    <li><span>Tom Kha Chicken *</span><span class="price">$7.00</span></li>
  </ul>
  <h2 class="section-title" style="left:15px;top:225px">CURRY <span class="swirl" role="img" aria-label="swirl ornament"></span></h2>
  <ul class="dish-list col1" style="top:251px;left:15px;width:200px">
    <li><span>Green curri Chicken</span><span class="price">$12.90</span></li>
    <li><span>Panang Chicken*</span><span class="price">$12.90</span></li>
    <li><span>Red Curry beef*</span><span class="price">$12.90</span></li>
    <li><span>Massaman beef Curry</span><span class="price">$12.90</span></li>
    <li><span>Red duck Curry</span><span class="price">$16.90</span></li>
    <li><span>Yellow Curry Chicken*</span><span class="price">$12.90</span></li>
    <li><span>Yellow Curry Prawn</span><span class="price">$16.90</span></li>
  </ul>
  <h2 class="section-title" style="left:18px;top:337px">VEGETABLE <span class="swirl" role="img" aria-label="swirl ornament"></span></h2>
  <ul class="dish-list col1" style="top:365px;left:15px;width:200px">
    <li><span>Mixed vegetables*</span><span class="price">$10.50</span></li>
    <li><span>Steamed veg/w Penaut Sauce*</span><span class="price">$10.50</span></li>
  </ul>
  <h2 class="section-title" style="left:21px;top:397px">BEEF <span class="swirl" role="img" aria-label="swirl ornament"></span></h2>
  <ul class="dish-list col1" style="top:422px;left:19px;width:196px">
    <li><span>Beef/w Oyster sauce*</span><span class="price">$12.90</span></li>
    <li><span>Grilled Beef salad*</span><span class="price">$12.90</span></li>
  </ul>
  <p class="notice abs" style="left:0;width:220px;top:452px">*Free delivery with in 5km-<br>minimum orders $40</p>

  <h2 class="section-title" style="left:238px;top:56px">CHICKEN <span class="swirl" role="img" aria-label="swirl ornament"></span></h2>
  <ul class="dish-list col2" style="top:86px">
    <li><span>Laab Chicken*</span><span class="price">$12.90</span></li>
    <li><span>Chicken /w Sweet basil*</span><span class="price">$12.90</span></li>
    <li><span>Chicken / w Cashew Nuts*</span><span class="price">$12.90</span></li>
    <li><span>Grilled Chicken / w Salad</span><span class="price">$12.90</span></li>
    <li><span>Southern style Fried Chicken</span><span class="price">$12.90</span></li>
  </ul>
  <h2 class="section-title" style="left:243px;top:150px">PORK <span class="swirl" role="img" aria-label="swirl ornament"></span></h2>
  <ul class="dish-list col2" style="top:176px">
    <li><span>Sweet &amp; sour Pork*</span><span class="price">$12.90</span></li>
    <li><span>Garlic Pork</span><span class="price">$12.90</span></li>
    <li><span>Crispy Pork &nbsp;/ w Asain Greens*</span><span class="price">$12.90</span></li>
  </ul>
  <h2 class="section-title" style="left:243px;top:222px">DUCK <span class="swirl" role="img" aria-label="swirl ornament"></span></h2>
  <ul class="dish-list col2" style="top:250px">
    <li><span>Roast Duck/ w Vegetable &amp; Gravy</span><span class="price">$16.90</span></li>
    <li><span>Duck / w Sweet Basil</span><span class="price">$16.90</span></li>
    <li><span>Honey Glazed duck/ w Vegetable</span><span class="price">$16.90</span></li>
  </ul>
  <h2 class="section-title" style="left:246px;top:295px">SEAFOOD <span class="swirl" role="img" aria-label="swirl ornament"></span></h2>
  <ul class="dish-list col2" style="top:323px">
    <li><span>Garllic Prawn</span><span class="price">$16.90</span></li>
    <li><span>Tamarind Prawn</span><span class="price">$16.90</span></li>
    <li><span>Laab Fish</span><span class="price">$16.90</span></li>
    <li><span>Crispy Fish/ w Swwt Chilli salsa</span><span class="price">$16.90</span></li>
    <li><span>Chilli &amp; Lime Calamari salad</span><span class="price">$16.90</span></li>
    <li><span>salt &amp; Pepper Calamari</span><span class="price">$16.90</span></li>
    <li><span>Spicy Seafood</span><span class="price">$16.90</span></li>
    <li><span>Crispy barramound /w Green Mango</span><span class="price"></span></li>
    <li><span>salad (Seasonal)</span><span class="price">$22.90</span></li>
    <li><span>Soft shell Chilli Crab</span><span class="price">$22.90</span></li>
  </ul>
  <p class="dietary">gluten free and vegetatian<br>option available on most meal</p>

  <h2 class="section-title" style="left:463px;top:56px">NOODLE <span class="swirl" role="img" aria-label="swirl ornament"></span></h2>
  <ul class="dish-list col3" style="top:83px">
    <li><span>Pad Thai*</span><span class="price">$12.50</span></li>
    <li><span>Pad Thai Prawn</span><span class="price">$16.90</span></li>
    <li><span>Drunken Noodle*</span><span class="price">$12.50</span></li>
    <li><span>Pad See Eew*</span><span class="price">$12.50</span></li>
    <li><span>Beef Noodle Soup</span><span class="price">$12.50</span></li>
    <li><span>Seafood Laksa</span><span class="price">$16.90</span></li>
  </ul>
  <h2 class="section-title" style="left:463px;top:156px">RICE <span class="swirl" role="img" aria-label="swirl ornament"></span></h2>
  <ul class="dish-list col3" style="top:188px">
    <li><span>Rice (S)</span><span class="price">$2.50</span></li>
    <li><span>Rice (L)</span><span class="price">$3.50</span></li>
    <li><span>Coconaut Rice (S)</span><span class="price">$4.50</span></li>
    <li><span>Coconaut Rice (L)</span><span class="price">$5.50</span></li>
    <li><span>Fried rice</span><span class="price">$10.50</span></li>
    <li><span>Roti bread</span><span class="price">$3.50</span></li>
  </ul>
  <h2 class="section-title" style="left:464px;top:263px">DESSERT <span class="swirl" role="img" aria-label="swirl ornament"></span></h2>
  <ul class="dish-list col3" style="top:290px">
    <li><span>Black sticky rice / w</span><span class="price"></span></li>
    <li><span>Coconaut Cream</span><span class="price">$4.50</span></li>
    <li><span>Tapioca Pudding / w Lychee</span><span class="price">$4.50</span></li>
  </ul>
  <h2 class="section-title" style="left:466px;top:334px">DRINK <span class="swirl" role="img" aria-label="swirl ornament"></span></h2>
  <ul class="dish-list col3" style="top:362px;left:466px;width:190px">
    <li><span>Cola, Diet Cola, Orange,</span><span class="price"></span></li>
    <li><span>Lemonade, Lime - 375ml</span><span class="price">$2.00</span></li>
    <li><span>Cola,Orange, Lemonade- 1.25L</span><span class="price">$4.50</span></li>
    <li><span>Orange Juice, Apple Juice</span><span class="price">$3.50</span></li>
    <li><span>Ginger Beer</span><span class="price">$3.50</span></li>
  </ul>
  <div class="brand brand--small">SAWAN</div>
</section>

</body>
</html>
```